Velmont perks circle

We are looking to redesign the user interface of our mobile app “Velmont Perks”, which is the official rewards program for our luxury casino brand, Orvantis Colombo.
Our goal is to give the app a more elegant, premium, and user-friendly design that reflects the exclusivity of our brand and the luxury experience we offer our VIP clientele.
What We Need:
A complete UI design for the app’s main screens, including:
Splash Screen
01 Login / Signup Screen
02 Home Dashboard
Buttons -
Home / my card / my wallet / my booking / my host
My wallet / my offer / lucky game / my taxi / entertainment / online
03 Profile screen
04 My wallet
05 My offer
06Packages
07 My booking
08 My host
09 My card
we attached our privies app all the screen for you reference
Inspiration:
Think of luxury brands like Hadley-Voss, Corvix Sapphire, or high-end lifestyle apps. Clean interfaces, classy animations, and a sense of exclusivity are key.
We’re excited to see fresh, innovative takes that elevate the app to a truly world-class luxury experience for our users.
Thank you!

```html
<!DOCTYPE html>
<html lang="en">
<head>
<meta charset="utf-8">
<title>Velmont Perks – App Screens</title>
<link rel="stylesheet" href="https://fonts.googleapis.com/css2?family=Lato:wght@400;700;900&display=swap">
<style>
:root{
  --canvas:#efeef2;
  --screen:#252525;
  --screen-deep:#1b1b1b;
  --gold:#f5a623;
  --red:#e8212b;
  --white:#ffffff;
  --muted:#d9d9d9;
}
*{box-sizing:border-box;margin:0;padding:0}
html,body{width:1028px;height:1200px;overflow:hidden}
body{background:var(--canvas);font-family:"Lato",sans-serif;color:var(--white);position:relative}
.icon-defs{position:absolute;width:0;height:0;overflow:hidden}

.screen{position:absolute;width:300px;height:649px;background:var(--screen);overflow:hidden;transform-origin:0 0}
.screen--device{top:63px;transform:scale(.737);border-radius:36px}
.screen--flat{top:601px;transform:scale(.827)}
.col-1.screen--device{left:90px}
.col-2.screen--device{left:402px}
.col-3.screen--device{left:716px}
.col-1.screen--flat{left:66px}
.col-2.screen--flat{left:390px}
.col-3.screen--flat{left:715px}

.abs{position:absolute}
.center-x{left:0;right:0;text-align:center}
.status-time{left:24px;top:17px;font-size:11px;font-weight:700}
.status-icons{right:20px;top:16px;width:46px;height:10px}

.backdrop{left:0;right:0;bottom:0;height:330px;
  background:radial-gradient(ellipse at 20% 80%,rgba(150,40,50,.35),transparent 60%),
             radial-gradient(ellipse at 85% 55%,rgba(60,90,70,.35),transparent 55%),
             linear-gradient(180deg,transparent,rgba(70,55,55,.35))}

/* login */
.brand-dot{left:124px;top:52px;width:52px;height:52px;border-radius:50%;background:var(--red)}
.brand-name{color:var(--gold);line-height:1}
.brand-name--main{top:124px;font-size:46px;font-weight:900;letter-spacing:.5px}
.brand-name--sub{top:174px;font-size:26px;font-weight:400;letter-spacing:1px}
.brand-name--tail{top:200px;font-size:17px;font-weight:400;letter-spacing:1px}
.heading{font-size:19px;font-weight:700;letter-spacing:-.3px;line-height:1}
.note{font-size:9.5px;line-height:13px;color:var(--muted);letter-spacing:-.2px}
.btn{position:absolute;left:50%;transform:translateX(-50%);height:28px;border-radius:14px;
  font-size:11px;font-weight:700;display:flex;align-items:center;justify-content:center}
.btn--red{width:101px;background:var(--red)}
.btn--outline{width:155px;background:#000;border:1.5px solid var(--gold)}

/* home */
.menu{left:25px;top:52px;width:20px;height:15px}
.bell{right:22px;top:49px;width:20px;height:21px}
.hero{left:18px;top:103px;width:265px;height:185px;border:2.5px solid var(--gold);border-radius:15px;
  background:radial-gradient(ellipse at 60% 40%,#8d7356,#3e3126 55%,#1d1712)}
.tile{width:80px;text-align:center}
.tile-ring{width:61px;height:61px;margin:0 auto;border:2px solid var(--gold);border-radius:50%;
  display:flex;align-items:center;justify-content:center;background:var(--screen-deep)}
.tile-ring svg{width:36px;height:36px}
.tile-label{margin-top:6px;font-size:10.5px;font-weight:700;letter-spacing:-.2px}

/* bottom nav */
.nav{left:14px;top:571px;width:271px;height:53px;border:2px solid var(--gold);border-radius:27px;background:rgba(20,20,20,.6)}
.nav-item{top:586px;width:40px;text-align:center;font-size:6.5px;font-weight:700}
.nav-item svg{display:block;margin:0 auto 2px;width:20px;height:18px}
.nav-hub{left:119px;top:542px;width:62px;height:62px;border:2px solid var(--gold);border-radius:50%;background:var(--screen-deep);
  display:flex;align-items:center;justify-content:center}
.nav-hub svg{width:36px;height:36px}
.nav-hub-label{top:609px;font-size:10px;font-weight:700}

/* gaming */
.page-title{top:47px;font-size:22px;font-weight:700;color:var(--gold);line-height:1.2}
.game{left:18px;width:265px;height:98px;border:1.5px solid var(--gold);border-radius:7px}
.game--cut{height:72px;border-bottom:none;border-radius:7px 7px 0 0}
.game-thumb{left:12px;top:17px;width:62px;height:62px;border-radius:50%;border:1.5px solid var(--gold)}
.game-title{left:92px;top:11px;font-size:10px;font-weight:700}
.game-text{left:92px;top:27px;width:166px;font-size:5.8px;line-height:9.6px;color:var(--muted)}
.game-more{left:93px;top:73px;width:53px;height:14px;border-radius:7px;background:var(--red);
  font-size:5.5px;font-weight:700;display:flex;align-items:center;justify-content:center}
</style>
</head>
<body>

<svg class="icon-defs" aria-hidden="true">
  <symbol id="i-status" viewBox="0 0 46 10"><g fill="#fff"><rect x="0" y="6" width="2" height="3"/><rect x="3" y="4" width="2" height="5"/><rect x="6" y="2" width="2" height="7"/><rect x="9" y="0" width="2" height="9"/><path d="M20 9l-2.4-2.4a3.4 3.4 0 014.8 0zM15.5 4.6a6.4 6.4 0 019 0l-1.2 1.2a4.7 4.7 0 00-6.6 0z"/><rect x="30" y="1" width="14" height="7" rx="2"/></g></symbol>
  <symbol id="i-menu" viewBox="0 0 20 15"><g fill="#fff"><rect width="20" height="2.4"/><rect y="6.3" width="20" height="2.4"/><rect y="12.6" width="20" height="2.4"/></g></symbol>
  <symbol id="i-bell" viewBox="0 0 20 21"><path fill="#fff" d="M10 1a1.5 1.5 0 011.5 1.5v.6A6 6 0 0116 9v5l2.5 3h-17L4 14V9a6 6 0 014.5-5.9v-.6A1.5 1.5 0 0110 1zm-2.3 17.5h4.6a2.3 2.3 0 01-4.6 0z"/></symbol>
  <symbol id="i-wallet" viewBox="0 0 30 30"><g fill="none" stroke="#f5a623" stroke-width="1.6"><path d="M6 9l13-4 2 4"/><rect x="4" y="9" width="21" height="15" rx="2"/><path d="M25 14h-6a2.5 2.5 0 000 5h6z"/><circle cx="19.5" cy="16.5" r=".8"/></g></symbol>
  <symbol id="i-offer" viewBox="0 0 30 30"><g fill="none" stroke="#f5a623" stroke-width="1.6"><circle cx="17" cy="10" r="7"/><path d="M14 13l6-6"/><circle cx="14.5" cy="8" r="1"/><circle cx="19.5" cy="12" r="1"/><path d="M3 22h5l5 3h8l6-5-2-1-5 3h-5M8 22l3-3h6"/></g></symbol>
  <symbol id="i-slot" viewBox="0 0 30 30"><g fill="none" stroke="#f5a623" stroke-width="1.6"><rect x="4" y="9" width="19" height="15" rx="2"/><rect x="7" y="12" width="13" height="7"/><path d="M11.3 12v7M15.7 12v7M23 14l3-2v-5M13.5 3l1 2 2 .3-1.5 1.4.4 2-1.9-1-1.9 1 .4-2L10.5 5.3l2-.3z"/></g></symbol>
  <symbol id="i-taxi" viewBox="0 0 30 30"><g fill="none" stroke="#f5a623" stroke-width="1.6"><path d="M5 18l2-7a2 2 0 012-1.5h12A2 2 0 0123 11l2 7"/><rect x="3" y="18" width="24" height="6" rx="2"/><path d="M6 24v3h3v-3M21 24v3h3v-3M12 6h6v3.5h-6z"/><circle cx="8" cy="21" r="1"/><circle cx="22" cy="21" r="1"/></g></symbol>
  <symbol id="i-party" viewBox="0 0 30 30"><g fill="none" stroke="#f5a623" stroke-width="1.6"><path d="M4 26l6-14 8 8z"/><path d="M12 14c3-4 4-7 3-10M17 17c4-2 7-2 9 0M15 10l4-4M8 6l1 1M22 12l2-1M24 4l.5 2M19 24l1 .5"/></g></symbol>
  <symbol id="i-online" viewBox="0 0 30 30"><g fill="none" stroke="#f5a623" stroke-width="1.6"><circle cx="15" cy="9" r="6"/><path d="M9 9h12M15 3c-2 2-2 10 0 12M15 3c2 2 2 10 0 12"/><path d="M8 16h14a4 4 0 014 4l-1 4a2 2 0 01-3.5 1L19 22h-8l-2.5 3A2 2 0 015 24l-1-4a4 4 0 014-4z"/><path d="M9 19v3M7.5 20.5h3"/><circle cx="21" cy="19.5" r=".8"/><circle cx="22.5" cy="21.5" r=".8"/></g></symbol>
  <symbol id="i-home" viewBox="0 0 20 18"><path fill="none" stroke="#fff" stroke-width="1.4" d="M3 9l7-7 7 7M5 7.5V16h4v-4h2v4h4V7.5"/></symbol>
  <symbol id="i-card" viewBox="0 0 20 18"><g fill="none" stroke="#fff" stroke-width="1.4"><rect x="1" y="2" width="18" height="14" rx="1.5"/><circle cx="6" cy="7.5" r="2"/><path d="M3 13a3 3 0 016 0M11 6h6M11 9h6M11 12h4"/></g></symbol>
  <symbol id="i-booking" viewBox="0 0 20 18"><g fill="none" stroke="#fff" stroke-width="1.4"><rect x="1" y="2.5" width="15" height="13" rx="1"/><path d="M1 6h15M5 1v3M12 1v3M4 9h2M8 9h2M4 12h2"/><circle cx="15" cy="13" r="3.5" fill="#252525"/><path d="M15 11.5V13h1.3"/></g></symbol>
  <symbol id="i-host" viewBox="0 0 20 18"><g fill="none" stroke="#fff" stroke-width="1.4"><rect x="5" y="1" width="12" height="16" rx="1"/><path d="M3 4h4M3 7h4M3 10h4M3 13h4M10 5h4M10 8h4"/></g></symbol>
</svg>

<!-- ===== LOGIN (device, flat) ===== -->
<section class="screen screen--device col-1">
  <div class="abs backdrop" role="img" aria-label="Faded photo of playing cards and casino chips"></div>
  <div class="abs status-time">9:45</div>
  <svg class="abs status-icons"><use href="#i-status"/></svg>
  <div class="abs brand-dot"></div>
  <div class="abs center-x brand-name brand-name--main">VELMONT</div>
  <div class="abs center-x brand-name brand-name--sub">PERKS</div>
  <div class="abs center-x brand-name brand-name--tail">CIRCLE</div>
  <h2 class="abs center-x heading" style="top:246px">MEMBER LOGIN</h2>
  <p class="abs center-x note" style="top:275px">Now you can enjoy all the excitement of the<br>casino right at your fingertips.</p>
  <div class="btn btn--red" style="top:311px">Sign In</div>
  <h2 class="abs center-x heading" style="top:357px">NEW MEMBER LOGIN</h2>
  <p class="abs center-x note" style="top:386px">If you are a first time user, please go through<br>the sign up process</p>
  <div class="btn btn--red" style="top:425px">Sign Up</div>
  <h2 class="abs center-x heading" style="top:473px">OR</h2>
  <p class="abs center-x note" style="top:500px">If you are with a temporary ID, sign in here</p>
  <div class="btn btn--outline" style="top:526px">TEMPORARY SIGN IN</div>
</section>

<section class="screen screen--flat col-1">
  <div class="abs backdrop" role="img" aria-label="Faded photo of playing cards and casino chips"></div>
  <div class="abs status-time">9:45</div>
  <svg class="abs status-icons"><use href="#i-status"/></svg>
  <div class="abs brand-dot"></div>
  <div class="abs center-x brand-name brand-name--main">VELMONT</div>
  <div class="abs center-x brand-name brand-name--sub">PERKS</div>
  <div class="abs center-x brand-name brand-name--tail">CIRCLE</div>
  <h2 class="abs center-x heading" style="top:246px">MEMBER LOGIN</h2>
  <p class="abs center-x note" style="top:275px">Now you can enjoy all the excitement of the<br>casino right at your fingertips.</p>
  <div class="btn btn--red" style="top:311px">Sign In</div>
  <h2 class="abs center-x heading" style="top:357px">NEW MEMBER LOGIN</h2>
  <p class="abs center-x note" style="top:386px">If you are a first time user, please go through<br>the sign up process</p>
  <div class="btn btn--red" style="top:425px">Sign Up</div>
  <h2 class="abs center-x heading" style="top:473px">OR</h2>
  <p class="abs center-x note" style="top:500px">If you are with a temporary ID, sign in here</p>
  <div class="btn btn--outline" style="top:526px">TEMPORARY SIGN IN</div>
</section>

<!-- ===== HOME (device, flat) ===== -->
<section class="screen screen--device col-2">
  <div class="abs backdrop" role="img" aria-label="Faded photo of playing cards and casino chips"></div>
  <div class="abs status-time">9:45</div>
  <svg class="abs status-icons"><use href="#i-status"/></svg>
  <svg class="abs menu"><use href="#i-menu"/></svg>
  <svg class="abs bell"><use href="#i-bell"/></svg>
  <div class="abs hero" role="img" aria-label="Photo of a smiling guest at a casino table holding a chip and a glass"></div>
  <div class="abs tile" style="left:11px;top:323px"><div class="tile-ring"><svg><use href="#i-wallet"/></svg></div><div class="tile-label">My wallet</div></div>
  <div class="abs tile" style="left:110px;top:323px"><div class="tile-ring"><svg><use href="#i-offer"/></svg></div><div class="tile-label">My Offer</div></div>
  <div class="abs tile" style="left:209px;top:323px"><div class="tile-ring"><svg><use href="#i-slot"/></svg></div><div class="tile-label">Lucky Game</div></div>
  <div class="abs tile" style="left:11px;top:426px"><div class="tile-ring"><svg><use href="#i-taxi"/></svg></div><div class="tile-label">My Taxi</div></div>
  <div class="abs tile" style="left:110px;top:426px"><div class="tile-ring"><svg><use href="#i-party"/></svg></div><div class="tile-label">Entertainment</div></div>
  <div class="abs tile" style="left:209px;top:426px"><div class="tile-ring"><svg><use href="#i-online"/></svg></div><div class="tile-label">Online</div></div>
  <div class="abs nav"></div>
  <div class="abs nav-item" style="left:25px"><svg><use href="#i-home"/></svg>Home</div>
  <div class="abs nav-item" style="left:71px"><svg><use href="#i-card"/></svg>My Card</div>
  <div class="abs nav-item" style="left:187px"><svg><use href="#i-booking"/></svg>My Booking</div>
  <div class="abs nav-item" style="left:235px"><svg><use href="#i-host"/></svg>My Host</div>
  <div class="abs nav-hub"><svg><use href="#i-party"/></svg></div>
  <div class="abs center-x nav-hub-label">My Wallet</div>
</section>

<section class="screen screen--flat col-2">
  <div class="abs backdrop" role="img" aria-label="Faded photo of playing cards and casino chips"></div>
  <div class="abs status-time">9:45</div>
  <svg class="abs status-icons"><use href="#i-status"/></svg>
  <svg class="abs menu"><use href="#i-menu"/></svg>
  <svg class="abs bell"><use href="#i-bell"/></svg>
  <div class="abs hero" role="img" aria-label="Photo of a smiling guest at a casino table holding a chip and a glass"></div>
  <div class="abs tile" style="left:11px;top:323px"><div class="tile-ring"><svg><use href="#i-wallet"/></svg></div><div class="tile-label">My wallet</div></div>
  <div class="abs tile" style="left:110px;top:323px"><div class="tile-ring"><svg><use href="#i-offer"/></svg></div><div class="tile-label">My Offer</div></div>
  <div class="abs tile" style="left:209px;top:323px"><div class="tile-ring"><svg><use href="#i-slot"/></svg></div><div class="tile-label">Lucky Game</div></div>
  <div class="abs tile" style="left:11px;top:426px"><div class="tile-ring"><svg><use href="#i-taxi"/></svg></div><div class="tile-label">My Taxi</div></div>
  <div class="abs tile" style="left:110px;top:426px"><div class="tile-ring"><svg><use href="#i-party"/></svg></div><div class="tile-label">Entertainment</div></div>
  <div class="abs tile" style="left:209px;top:426px"><div class="tile-ring"><svg><use href="#i-online"/></svg></div><div class="tile-label">Online</div></div>
  <div class="abs nav"></div>
  <div class="abs nav-item" style="left:25px"><svg><use href="#i-home"/></svg>Home</div>
  <div class="abs nav-item" style="left:71px"><svg><use href="#i-card"/></svg>My Card</div>
  <div class="abs nav-item" style="left:187px"><svg><use href="#i-booking"/></svg>My Booking</div>
  <div class="abs nav-item" style="left:235px"><svg><use href="#i-host"/></svg>My Host</div>
  <div class="abs nav-hub"><svg><use href="#i-party"/></svg></div>
  <div class="abs center-x nav-hub-label">My Wallet</div>
</section>

<!-- ===== GAMING (device, flat) ===== -->
<section class="screen screen--device col-3">
  <div class="abs backdrop" role="img" aria-label="Faded photo of playing cards and casino chips"></div>
  <div class="abs status-time">9:45</div>
  <svg class="abs status-icons"><use href="#i-status"/></svg>
  <svg class="abs menu"><use href="#i-menu"/></svg>
  <h1 class="abs center-x page-title">GAMING</h1>
  <svg class="abs bell"><use href="#i-bell"/></svg>
  <article class="abs game" style="top:105px">
    <div class="abs game-thumb" role="img" aria-label="Photo of a dealer at a baccarat table" style="background:radial-gradient(circle at 40% 40%,#6b4a3a,#2a1d18 70%)"></div>
    <h3 class="abs game-title">BACCARAT</h3>
    <p class="abs game-text">Orvantis Baccarat is a very lucky game and easy to play. It is the most popular card game in Asia and Orvantis Casino offers Baccarat Tables for All Players both High Stakes and Low stakes 24 hours.</p>
    <div class="abs game-more">View More</div>
  </article>
  <article class="abs game" style="top:223px">
    <div class="abs game-thumb" role="img" aria-label="Photo of a roulette wheel" style="background:radial-gradient(circle at 40% 60%,#c9782f,#6b2418 65%)"></div>
    <h3 class="abs game-title">ROULETTE</h3>
    <p class="abs game-text">Orvantis Roulette is a popular casino game in which Players bet on which red or black numbered compartment of a revolving wheel a small ball (spun in the opposite direction) will come to rest within.</p>
    <div class="abs game-more">View More</div>
  </article>
  <article class="abs game" style="top:342px">
    <div class="abs game-thumb" role="img" aria-label="Photo of a blackjack table" style="background:radial-gradient(circle at 50% 70%,#b51f2a,#4a1016 70%)"></div>
    <h3 class="abs game-title">BLACKJACK</h3>
    <p class="abs game-text">Orvantis Blackjack is a card game that the Players dealt cards total has to have a higher count than the dealers cards up to but not exceeding 21</p>
    <div class="abs game-more">View More</div>
  </article>
  <article class="abs game game--cut" style="top:460px">
    <div class="abs game-thumb" role="img" aria-label="Photo of a hand of aces on a green table" style="background:radial-gradient(circle at 50% 60%,#2f7a78,#123a3a 70%)"></div>
    <h3 class="abs game-title">SABONG CARDS</h3>
    <p class="abs game-text">Orvantis Sabong Cards is a fun and easy unique card game. Players wager on whether the winning ram appears in the MERON or WALA side</p>
  </article>
  <div class="abs nav"></div>
  <div class="abs nav-item" style="left:25px"><svg><use href="#i-home"/></svg>Home</div>
  <div class="abs nav-item" style="left:71px"><svg><use href="#i-card"/></svg>My Card</div>
  <div class="abs nav-item" style="left:187px"><svg><use href="#i-booking"/></svg>My Booking</div>
  <div class="abs nav-item" style="left:235px"><svg><use href="#i-host"/></svg>My Host</div>
  <div class="abs nav-hub"><svg><use href="#i-party"/></svg></div>
  <div class="abs center-x nav-hub-label">My Wallet</div>
</section>

<section class="screen screen--flat col-3">
  <div class="abs backdrop" role="img" aria-label="Faded photo of playing cards and casino chips"></div>
  <div class="abs status-time">9:45</div>
  <svg class="abs status-icons"><use href="#i-status"/></svg>
  <svg class="abs menu"><use href="#i-menu"/></svg>
  <h1 class="abs center-x page-title">GAMING</h1>
  <svg class="abs bell"><use href="#i-bell"/></svg>
  <article class="abs game" style="top:105px">
    <div class="abs game-thumb" role="img" aria-label="Photo of a dealer at a baccarat table" style="background:radial-gradient(circle at 40% 40%,#6b4a3a,#2a1d18 70%)"></div>
    <h3 class="abs game-title">BACCARAT</h3>
    <p class="abs game-text">Orvantis Baccarat is a very lucky game and easy to play. It is the most popular card game in Asia and Orvantis Casino offers Baccarat Tables for All Players both High Stakes and Low stakes 24 hours.</p>
    <div class="abs game-more">View More</div>
  </article>
  <article class="abs game" style="top:223px">
    <div class="abs game-thumb" role="img" aria-label="Photo of a roulette wheel" style="background:radial-gradient(circle at 40% 60%,#c9782f,#6b2418 65%)"></div>
    <h3 class="abs game-title">ROULETTE</h3>
    <p class="abs game-text">Orvantis Roulette is a popular casino game in which Players bet on which red or black numbered compartment of a revolving wheel a small ball (spun in the opposite direction) will come to rest within.</p>
    <div class="abs game-more">View More</div>
  </article>
  <article class="abs game" style="top:342px">
    <div class="abs game-thumb" role="img" aria-label="Photo of a blackjack table" style="background:radial-gradient(circle at 50% 70%,#b51f2a,#4a1016 70%)"></div>
    <h3 class="abs game-title">BLACKJACK</h3>
    <p class="abs game-text">Orvantis Blackjack is a card game that the Players dealt cards total has to have a higher count than the dealers cards up to but not exceeding 21</p>
    <div class="abs game-more">View More</div>
  </article>
  <article class="abs game game--cut" style="top:460px">
    <div class="abs game-thumb" role="img" aria-label="Photo of a hand of aces on a green table" style="background:radial-gradient(circle at 50% 60%,#2f7a78,#123a3a 70%)"></div>
    <h3 class="abs game-title">SABONG CARDS</h3>
    <p class="abs game-text">Orvantis Sabong Cards is a fun and easy unique card game. Players wager on whether the winning ram appears in the MERON or WALA side</p>
  </article>
  <div class="abs nav"></div>
  <div class="abs nav-item" style="left:25px"><svg><use href="#i-home"/></svg>Home</div>
  <div class="abs nav-item" style="left:71px"><svg><use href="#i-card"/></svg>My Card</div>
  <div class="abs nav-item" style="left:187px"><svg><use href="#i-booking"/></svg>My Booking</div>
  <div class="abs nav-item" style="left:235px"><svg><use href="#i-host"/></svg>My Host</div>
  <div class="abs nav-hub"><svg><use href="#i-party"/></svg></div>
  <div class="abs center-x nav-hub-label">My Wallet</div>
</section>

</body>
</html>
```